Ridge Gathering presented by The Lantern

This is a one-day seminar for men who want to grow mentally, spiritually and financially.
Host Pastor Gordon Whitlock
Special guest: Dr. Frank Dunmore, Dr. Brenda Soward

Target Market(s)

Men 18-55

Colors

Designer to choose colors to be used in the design.

Requirements
Must have
• clean designs
Nice to have
• A clean design that translates to social media and websites

```html
<!DOCTYPE html>
<html lang="en">
<head>
<meta charset="UTF-8">
<title>Ridge Gathering – One Day Seminar</title>
<link href="https://fonts.googleapis.com/css2?family=Archivo+Black&family=Arimo:wght@400;700&family=Kaushan+Script&display=swap" rel="stylesheet">
<style>
  :root {
    --navy: #232b78;
    --navy-deep: #1a2066;
    --navy-light: #2c3585;
    --ink: #10354f;
    --yellow: #f5cf0a;
    --white: #ffffff;
    --backdrop: #e9e9ec;
    --photo-a: #d9d6d4;
    --photo-b: #8a8582;
  }
  * { margin: 0; padding: 0; box-sizing: border-box; }
  html, body { width: 1200px; height: 1200px; overflow: hidden; background: var(--backdrop); }
  .canvas { position: relative; width: 1200px; height: 1200px; }
  .poster {
    position: absolute; left: 191px; top: 25px; width: 818px; height: 1150px;
    background: linear-gradient(160deg, var(--navy-light) 0%, var(--navy) 45%, var(--navy-deep) 100%);
    overflow: hidden; font-family: "Arimo", Arial, sans-serif; color: var(--white);
  }
  .invite {
    position: absolute; top: 160px; width: 100%; text-align: center;
    font-family: "Kaushan Script", cursive; font-size: 58px; line-height: 1;
    transform: translateY(-50%);
  }
  .headline {
    position: absolute; top: 200px; left: 0; width: 100%; text-align: center;
    font-family: "Archivo Black", "Arial Black", sans-serif; font-size: 126px;
    line-height: 1; color: var(--yellow); letter-spacing: 1px;
  }
  .rule { position: absolute; left: 92px; width: 644px; height: 7px; background: var(--white); }
  .rule--top { top: 333px; }
  .rule--bottom { top: 438px; }
  .subhead {
    position: absolute; top: 350px; left: 92px; width: 660px;
    font-family: "Archivo Black", "Arial Black", sans-serif; font-size: 84px; line-height: 1;
    color: var(--yellow); letter-spacing: 30px; text-align: center;
  }
  .date-ribbon { position: absolute; left: 0; top: 488px; width: 818px; height: 115px; }
  .date-text {
    position: absolute; top: 494px; left: 125px; width: 547px; height: 67px;
    display: flex; align-items: center; justify-content: center;
    font-family: "Archivo Black", "Arial Black", sans-serif; font-size: 45px; color: var(--ink);
  }
  .speaker { position: absolute; top: 645px; width: 260px; text-align: center; }
  .speaker__photo { display: block; width: 250px; height: 250px; margin: 0 auto; }
  .speaker__name { margin-top: 8px; font-weight: 700; font-size: 23px; line-height: 32px; }
  .speaker--host { left: 27px; }
  .speaker--guest-one { left: 288px; top: 647px; }
  .speaker--guest-two { left: 545px; }
  .guest-bracket { position: absolute; left: 385px; top: 938px; width: 342px; height: 104px; }
  .guest-label {
    position: absolute; top: 1018px; left: 423px; width: 260px; text-align: center;
    font-weight: 700; font-size: 23px; letter-spacing: 1px;
  }
  .footer-band {
    position: absolute; left: 0; bottom: 0; width: 100%; height: 76px; background: var(--yellow);
    color: #111; font-size: 17px; display: flex; align-items: flex-start; justify-content: center;
    padding-top: 16px;
  }
</style>
</head>
<body>
<div class="canvas">
  <div class="poster">
    <div class="invite">Join Us for</div>
    <div class="headline">ONE DAY</div>
    <div class="rule rule--top"></div>
    <div class="subhead">SEMINAR</div>
    <div class="rule rule--bottom"></div>

    <svg class="date-ribbon" viewBox="0 0 818 115" aria-hidden="true">
      <polygon points="65,40 165,40 165,107 65,107 90,73" fill="#ffffff"/>
      <polygon points="627,36 728,36 700,70 728,103 627,103" fill="#ffffff"/>
      <rect x="123" y="4" width="551" height="71" fill="#ffffff" stroke="#1a2066" stroke-width="3"/>
    </svg>
    <div class="date-text">23 AUGUST @ 12PM</div>

    <div class="speaker speaker--host">
      <svg class="speaker__photo" viewBox="0 0 250 250" role="img" aria-label="Portrait photo of Host Pastor Gordon Whitlock">
        <defs><linearGradient id="photoHost" x1="0" y1="0" x2="0" y2="1"><stop offset="0" stop-color="#dcd8d6"/><stop offset="1" stop-color="#b9b3ae"/></linearGradient></defs>
        <circle cx="125" cy="125" r="121" fill="#f5cf0a"/>
        <circle cx="119" cy="120" r="115" fill="url(#photoHost)"/>
      </svg>
      <div class="speaker__name">Host Pastor<br>Gordon Whitlock</div>
    </div>

    <div class="speaker speaker--guest-one">
      <svg class="speaker__photo" viewBox="0 0 250 250" role="img" aria-label="Portrait photo of Dr. Frank Dunmore">
        <defs><linearGradient id="photoOne" x1="0" y1="0" x2="0" y2="1"><stop offset="0" stop-color="#f4f4f6"/><stop offset="1" stop-color="#5a638f"/></linearGradient></defs>
        <circle cx="125" cy="125" r="121" fill="#f5cf0a"/>
        <circle cx="119" cy="120" r="115" fill="url(#photoOne)"/>
      </svg>
      <div class="speaker__name">Dr. Frank Dunmore</div>
    </div>

    <div class="speaker speaker--guest-two">
      <svg class="speaker__photo" viewBox="0 0 250 250" role="img" aria-label="Portrait photo of Dr. Brenda Soward">
        <defs><linearGradient id="photoTwo" x1="0" y1="0" x2="0" y2="1"><stop offset="0" stop-color="#f7f7f7"/><stop offset="1" stop-color="#3a3a3a"/></linearGradient></defs>
        <circle cx="125" cy="125" r="121" fill="#f5cf0a"/>
        <circle cx="119" cy="120" r="115" fill="url(#photoTwo)"/>
      </svg>
      <div class="speaker__name">Dr. Brenda Soward</div>
    </div>

    <svg class="guest-bracket" viewBox="0 0 342 104" aria-hidden="true">
      <polyline points="3,0 3,100 45,100" fill="none" stroke="#ffffff" stroke-width="4"/>
      <polyline points="293,100 338,100 338,0" fill="none" stroke="#ffffff" stroke-width="4"/>
    </svg>
    <div class="guest-label">SPECIAL GUESTS</div>

    <div class="footer-band">This is a one-day seminar for men who want to grow mentally, spiritually and financially.</div>
  </div>
</div>
</body>
</html>
```